Business Card Re-design

We are looking for a fresh bold look for general office business cards. We are a staffing agency that staffs industrial, coal mining, and clerical jobs.
Tag Line: Reliable people for every shift, every day.
Marrowfield Office: 2473 W. Tallow Creek Rd, Marrowfield, OH - 47308
p. 555.203.6180 f. 555.203.6195
Kestrel Falls Office: 264 S. Birch Ln, Kestrel Falls, OH - 47152
p. 555.319.2047 f. 555.203.6195
Absentee/Emergency 24hr Hotline 555.203.6172 opt.1
www.bluelanternworkforce.example

```html
<!DOCTYPE html>
<html lang="en">
<head>
<meta charset="utf-8">
<title>Blue Lantern Workforce – Business Cards</title>
<link href="https://fonts.googleapis.com/css2?family=Open+Sans:wght@400;700;800&display=swap" rel="stylesheet">
<style>
  :root {
    --navy: #123a6b;
    --green: #3a9a3e;
    --grey-text: #8a8a8a;
    --grey-dark: #6f6f6f;
    --card: #ffffff;
    --backdrop: #e9ecf1;
    --band-blue: rgba(120, 135, 170, 0.10);
    --band-green: rgba(140, 200, 120, 0.12);
  }
  * { box-sizing: border-box; margin: 0; padding: 0; }
  html, body { width: 1200px; height: 1200px; overflow: hidden; }
  body {
    background: var(--backdrop);
    font-family: "Open Sans", Arial, sans-serif;
    position: relative;
  }
  .card {
    position: absolute;
    width: 500px;
    height: 500px;
    background: var(--card);
    box-shadow: 0 6px 24px rgba(20, 40, 80, 0.18);
    overflow: hidden;
  }
  .card--front { left: 90px; top: 90px; }
  .card--back { left: 610px; top: 610px; }

  .brand {
    display: flex;
    align-items: center;
    gap: 14px;
    color: var(--navy);
    font-weight: 800;
    text-transform: uppercase;
    line-height: 1.02;
  }
  .brand__mark { flex: none; background: var(--navy); border-radius: 50%; }
  .card--front .brand { position: absolute; left: 70px; top: 110px; font-size: 46px; }
  .card--front .brand__mark { width: 30px; height: 30px; }

  .hotline {
    position: absolute;
    left: 0; right: 0; bottom: 70px;
    text-align: center;
    color: var(--grey-text);
  }
  .hotline__icon { width: 56px; height: 56px; margin: 0 auto 10px; display: block; }
  .hotline__label { font-weight: 700; font-size: 19px; }
  .hotline__number { font-size: 18px; }

  .bands { position: absolute; inset: 0; }

  .card--back .brand { position: absolute; left: 40px; top: 40px; font-size: 24px; gap: 10px; }
  .card--back .brand__mark { width: 16px; height: 16px; }

  .offices { position: absolute; left: 40px; top: 150px; right: 30px; color: var(--grey-dark); }
  .office { margin-bottom: 22px; }
  .office__title { display: flex; align-items: center; gap: 8px; font-weight: 700; font-size: 17px; color: var(--grey-dark); }
  .office__line { padding-left: 22px; font-size: 15px; line-height: 1.5; white-space: nowrap; }
  .office__contacts { padding-left: 22px; display: flex; gap: 26px; font-size: 15px; }
  .contact { display: flex; align-items: center; gap: 6px; }
  .icon { width: 14px; height: 14px; flex: none; }

  .website { display: flex; align-items: center; gap: 8px; font-size: 15px; color: var(--grey-dark); margin-top: 6px; }

  .tagline {
    position: absolute;
    left: 40px; right: 30px; bottom: 44px;
    color: var(--green);
    font-weight: 700;
    font-size: 18px;
    white-space: nowrap;
  }
</style>
</head>
<body>

<section class="card card--front" aria-label="Business card front">
  <div class="brand">
    <span class="brand__mark"></span>
    <span class="brand__name">Blue Lantern<br>Workforce</span>
  </div>
  <div class="hotline">
    <svg class="hotline__icon" viewBox="0 0 56 56" aria-hidden="true">
      <circle cx="28" cy="28" r="24" fill="none" stroke="#2f6fa8" stroke-width="4"/>
      <circle cx="28" cy="28" r="15" fill="#123a6b"/>
      <text x="28" y="33" text-anchor="middle" font-family="Open Sans, sans-serif" font-size="13" font-weight="700" fill="#fff">24h</text>
      <rect x="40" y="38" width="8" height="8" rx="2" fill="#3a9a3e"/>
    </svg>
    <div class="hotline__label">Absentee/Emergency (Hotline)</div>
    <div class="hotline__number">555.203.6172 opt.1</div>
  </div>
</section>

<section class="card card--back" aria-label="Business card back">
  <svg class="bands" viewBox="0 0 500 500" preserveAspectRatio="none" aria-hidden="true">
    <polygon points="330,0 440,0 160,500 50,500" fill="var(--band-blue)"/>
    <polygon points="460,0 500,0 500,60 250,500 210,500" fill="var(--band-green)"/>
  </svg>

  <div class="brand">
    <span class="brand__mark"></span>
    <span class="brand__name">Blue Lantern<br>Workforce</span>
  </div>

  <div class="offices">
    <div class="office">
      <div class="office__title">
        <svg class="icon" viewBox="0 0 14 14" aria-hidden="true"><path d="M7 1a4 4 0 0 0-4 4c0 3 4 8 4 8s4-5 4-8a4 4 0 0 0-4-4z" fill="none" stroke="#123a6b" stroke-width="2"/></svg>
        Marrowfield Office:
      </div>
      <div class="office__line">2473 W. Tallow Creek Rd, Marrowfield, OH - 47308</div>
      <div class="office__contacts">
        <span class="contact"><svg class="icon" viewBox="0 0 14 14" aria-hidden="true"><path d="M3 1l3 3-1.5 1.5a8 8 0 0 0 4 4L10 8l3 3-2 2C6 13 1 8 1 3z" fill="#123a6b"/></svg>555.203.6180</span>
        <span class="contact"><svg class="icon" viewBox="0 0 14 14" aria-hidden="true"><rect x="1" y="4" width="12" height="9" fill="#123a6b"/><rect x="4" y="1" width="6" height="4" fill="#123a6b"/></svg>555.203.6195</span>
      </div>
    </div>
    <div class="office">
      <div class="office__title">
        <svg class="icon" viewBox="0 0 14 14" aria-hidden="true"><path d="M7 1a4 4 0 0 0-4 4c0 3 4 8 4 8s4-5 4-8a4 4 0 0 0-4-4z" fill="none" stroke="#123a6b" stroke-width="2"/></svg>
        Kestrel Falls Office:
      </div>
      <div class="office__line">264 S. Birch Ln, Kestrel Falls, OH - 47152</div>
      <div class="office__contacts">
        <span class="contact"><svg class="icon" viewBox="0 0 14 14" aria-hidden="true"><path d="M3 1l3 3-1.5 1.5a8 8 0 0 0 4 4L10 8l3 3-2 2C6 13 1 8 1 3z" fill="#123a6b"/></svg>555.319.2047</span>
        <span class="contact"><svg class="icon" viewBox="0 0 14 14" aria-hidden="true"><rect x="1" y="4" width="12" height="9" fill="#123a6b"/><rect x="4" y="1" width="6" height="4" fill="#123a6b"/></svg>555.203.6195</span>
      </div>
    </div>
    <div class="website">
      <svg class="icon" viewBox="0 0 14 14" aria-hidden="true"><circle cx="7" cy="7" r="6" fill="none" stroke="#6f6f6f" stroke-width="1.4"/><path d="M1 7h12M7 1c3 3 3 9 0 12M7 1c-3 3-3 9 0 12" fill="none" stroke="#6f6f6f" stroke-width="1.2"/></svg>
      www.bluelanternworkforce.example
    </div>
  </div>

  <div class="tagline">Reliable people for every shift, every day</div>
</section>

</body>
</html>
```